Full Business Set-Up Stationary, Folder, Envelope, & Business Card, etc. CPA Firm
CPA Firm Collarteral Package
Full Business Set-Up Stationary, Folder, Envelope, & Business Card, etc. CPA Firm - Consulting
Creative Brief
Bright & Fun-filled
Marla Penn, CPA
Certified Public Accountant
512 Hadley Court Suite 200 Oakmere, FL 40217
MarlaPenn@ledgerbox.example
www.MarlaPennCPA.example
RT58163
Key Words: CPA since 1999 Servicing State of Florida since 1999 Certified Management Accountant Certified Public Accounting Firm Award Winning CPA Award Winning Professional Officies Located in the Oakmere Civic Trade Hall Trustworthy, Professional, Experienced
Tag Line: See the Clarity TrueMark Services
marlapenn marlapenn
Thanks for your submissions. Please include portfolio for the Firm. Particularly a Business Folder and Letterhead/Envelope. Ipad and Iphone Designs.

```html
<!DOCTYPE html>
<html lang="en">
<head>
<meta charset="utf-8">
<title>Marla Penn CPA – Business Card</title>
<link rel="stylesheet" href="https://fonts.googleapis.com/css2?family=Cinzel:wght@400;600&family=Cormorant+Garamond:wght@500;600&display=swap">
<style>
  :root {
    --bg: #8a8c8f;
    --blue-light: #4a9be3;
    --blue-dark: #1d67bf;
    --blue-mid: #2a7fd4;
    --green: #7cc242;
    --ink: #3b3f45;
    --ink-soft: #5a6068;
    --white: #ffffff;
  }
  * { margin: 0; padding: 0; box-sizing: border-box; }
  html, body { width: 1200px; height: 908px; overflow: hidden; }
  body {
    background: var(--bg);
    font-family: "Cormorant Garamond", Georgia, serif;
    position: relative;
  }
  .card {
    position: absolute;
    width: 540px;
    height: 310px;
    border-radius: 22px;
    overflow: hidden;
    box-shadow: 0 10px 24px rgba(0,0,0,0.28);
  }
  /* Front */
  .card-front {
    left: 50px; top: 140px;
    background: linear-gradient(160deg, var(--blue-light) 0%, var(--blue-mid) 55%, var(--blue-dark) 100%);
    color: var(--white);
  }
  .front-mark {
    position: absolute;
    right: 40px; top: 40px;
    width: 200px; height: 200px;
    border-radius: 50%;
    background: rgba(255,255,255,0.08);
  }
  .front-name {
    position: absolute;
    left: 38px; bottom: 82px;
    font-family: "Cinzel", "Times New Roman", serif;
    font-weight: 400;
    font-size: 30px;
    letter-spacing: 1px;
  }
  .front-tagline {
    position: absolute;
    left: 40px; bottom: 60px;
    font-family: "Cinzel", "Times New Roman", serif;
    font-size: 12px;
    letter-spacing: 5px;
  }
  /* Back */
  .card-back {
    left: 610px; top: 458px;
    background: var(--white);
    color: var(--ink);
  }
  .back-brand {
    position: absolute;
    left: 30px; bottom: 34px;
    display: flex; align-items: center; gap: 10px;
  }
  .brand-dot {
    width: 38px; height: 38px;
    border-radius: 50%;
    background: var(--green);
    flex: none;
  }
  .brand-name {
    font-family: "Cinzel", "Times New Roman", serif;
    font-size: 22px;
    line-height: 1.1;
    color: var(--ink);
    letter-spacing: 0.5px;
    white-space: nowrap;
  }
  .brand-tagline {
    font-family: "Cinzel", "Times New Roman", serif;
    font-size: 9px;
    letter-spacing: 4px;
    color: var(--ink);
    white-space: nowrap;
  }
  .contact {
    position: absolute;
    left: 232px; top: 36px;
    font-size: 13px;
    line-height: 1.35;
    color: var(--ink-soft);
    white-space: nowrap;
  }
  .contact-name {
    font-family: "Cinzel", "Times New Roman", serif;
    font-size: 18px;
    color: var(--blue-dark);
  }
  .contact-title {
    font-family: "Cinzel", "Times New Roman", serif;
    font-size: 9px;
    letter-spacing: 1px;
    color: var(--ink);
    margin-bottom: 6px;
  }
  .contact-license { font-size: 11px; margin-bottom: 4px; }
  .contact-row { display: flex; align-items: center; gap: 5px; }
  .contact-row svg { width: 9px; height: 9px; flex: none; }
  .swoosh { position: absolute; right: 0; top: 0; width: 140px; height: 310px; }
  .website {
    position: absolute;
    right: 10px; top: 155px;
    transform: translate(50%, -50%) rotate(-90deg);
    transform-origin: center;
    font-size: 13px;
    letter-spacing: 1px;
    color: var(--white);
    white-space: nowrap;
  }
</style>
</head>
<body>
  <section class="card card-front">
    <div class="front-mark"></div>
    <h1 class="front-name">MARLA PENN CPA</h1>
    <p class="front-tagline">SEE THE CLARITY</p>
  </section>

  <section class="card card-back">
    <div class="contact">
      <div class="contact-name">Marla Penn, CPA</div>
      <div class="contact-title">CERTIFIED PUBLIC ACCOUNTANT</div>
      <div class="contact-license">License No: RT58163</div>
      <div>512 Hadley Court Suite 200</div>
      <div>Oakmere, FL 40217</div>
      <div class="contact-row"><svg viewBox="0 0 10 10"><circle cx="5" cy="5" r="5" fill="#7cc242"/></svg>555-201-4470</div>
      <div class="contact-row"><svg viewBox="0 0 10 10"><circle cx="5" cy="5" r="5" fill="#7cc242"/></svg>555-201-4471</div>
      <div class="contact-row"><svg viewBox="0 0 10 10"><circle cx="5" cy="5" r="5" fill="#7cc242"/></svg>MarlaPenn@ledgerbox.example</div>
    </div>

    <div class="back-brand">
      <span class="brand-dot"></span>
      <div>
        <div class="brand-name">MARLA PENN CPA</div>
        <div class="brand-tagline">SEE THE CLARITY</div>
      </div>
    </div>

    <svg class="swoosh" viewBox="0 0 140 310" preserveAspectRatio="none">
      <path d="M140 0 L110 0 C70 90 70 200 0 310 L140 310 Z" fill="#7cc242"/>
      <path d="M140 0 L122 0 C88 90 90 210 28 310 L140 310 Z" fill="#ffffff"/>
      <path d="M140 0 L128 0 C98 90 100 210 42 310 L140 310 Z" fill="#2a7fd4"/>
    </svg>
    <div class="website">www.MarlaPennCPA.example</div>
  </section>
</body>
</html>
```